Whitcombe Framing Works - Card Design

I am looking to use the logo designs that you already did for me to develop a business card. I would like the card to have a black background and be double sided. I want white and green logo and text. I have attached an inspiration photo of a look that I like. I would like to use the Vertical Logo attached to take up the full front side of the card. On the back where I have my name and information, I would like to have the horizontal logo or maybe even just the image of the 'A' and trees without the text. I am open, but I am looking for something clean and simple and I want the green to really pop! Additional files can be found under Design #: 40593216

Target Market(s)

Homeowners

Industry/Entity Type

Construction

Contact Information for Business Card

Name: Marcus Pellow, Title: Project Manager, Phone: 831.555.0147, Email: whitcombeframingworks@mailbarn.net, address: 418 Juniper Ln, Felton, CA 95092, Lic# 2046318

Colors
00AB8E
00BBA5
67D7C9
C6EFE9
E9F9F6

Requirements
Nice to have
• I would like to see the logos that I have already got from SketchHarbor, though I am open to new ones

```html
<!DOCTYPE html>
<html lang="en">
<head>
<meta charset="utf-8">
<title>Whitcombe Framing Works – Business Card</title>
<link href="https://fonts.googleapis.com/css2?family=Jost:wght@400;500;600&display=swap" rel="stylesheet">
<style>
  :root {
    --backdrop: #939393;
    --card: #252525;
    --green: #41b14b;
    --white: #ffffff;
  }
  * { margin: 0; padding: 0; box-sizing: border-box; }
  html, body { width: 1200px; height: 1000px; overflow: hidden; }
  body {
    background: var(--backdrop);
    font-family: "Jost", "Futura", sans-serif;
    position: relative;
    color: var(--white);
  }
  .card {
    position: absolute;
    left: 293px;
    width: 615px;
    height: 351px;
    background: var(--card);
    border-radius: 30px;
  }
  .card--front { top: 104px; }
  .card--back { top: 504px; }

  .brand-lockup {
    position: absolute;
    left: 0; right: 0; top: 150px; height: 40px;
    display: flex; align-items: center; justify-content: center; gap: 14px;
  }
  .brand-dot {
    flex: none;
    width: 26px; height: 26px; border-radius: 50%;
    background: var(--green);
  }
  .brand-name {
    white-space: nowrap;
    font-weight: 600; font-size: 29px; letter-spacing: 1.5px; line-height: 1;
    color: var(--white); text-transform: uppercase;
  }

  .badge {
    position: absolute;
    left: 57px; top: 105px;
    width: 164px; height: 164px;
    border: 4px solid var(--white);
    border-radius: 50%;
    display: flex; align-items: center; justify-content: center;
    text-align: center;
  }
  .badge-name {
    font-weight: 600; font-size: 19px; line-height: 1.15; letter-spacing: 1px;
    color: var(--white); text-transform: uppercase;
  }
  .divider {
    position: absolute; left: 273px; top: 84px;
    width: 2px; height: 184px; background: var(--white);
  }
  .contact-name {
    position: absolute; left: 299px; top: 88px;
    color: var(--green); font-weight: 600; font-size: 20px; letter-spacing: 0.8px;
    text-transform: uppercase;
  }
  .contact-role {
    position: absolute; left: 300px; top: 117px;
    font-size: 12px; font-weight: 500; letter-spacing: 2px; line-height: 16px;
    text-transform: uppercase;
  }
  .contact-list {
    position: absolute; left: 301px; top: 182px; list-style: none;
  }
  .contact-list li {
    display: flex; align-items: center; gap: 6px;
    height: 20px; margin-bottom: 9px;
    font-size: 13px; font-weight: 500; letter-spacing: 0.3px; white-space: nowrap;
  }
  .contact-list li.upper { text-transform: uppercase; }
  .icon { width: 20px; height: 20px; flex: none; }
</style>
</head>
<body>
  <section class="card card--front">
    <div class="brand-lockup">
      <span class="brand-dot"></span>
      <span class="brand-name">Whitcombe Framing Works</span>
    </div>
  </section>

  <section class="card card--back">
    <div class="badge">
      <span class="badge-name">Whitcombe<br>Framing<br>Works</span>
    </div>
    <div class="divider"></div>
    <h1 class="contact-name">Marcus Pellow</h1>
    <p class="contact-role">Project Manager<br>Lic# 2046318</p>
    <ul class="contact-list">
      <li>
        <svg class="icon" viewBox="0 0 20 20"><circle cx="10" cy="10" r="10" fill="var(--green)"/><rect x="5" y="6.5" width="10" height="7" fill="#252525"/><path d="M5 6.5 L10 10.5 L15 6.5" stroke="var(--green)" stroke-width="1.2" fill="none"/></svg>
        whitcombeframingworks@mailbarn.net
      </li>
      <li>
        <svg class="icon" viewBox="0 0 20 20"><circle cx="10" cy="10" r="10" fill="var(--green)"/><path d="M6.5 5 L8.5 5 L9.3 7.6 L8.1 8.6 C8.8 10 10 11.2 11.4 11.9 L12.4 10.7 L15 11.5 L15 13.5 C15 14.3 14.3 15 13.5 15 C9.4 15 5 10.6 5 6.5 C5 5.7 5.7 5 6.5 5 Z" fill="#252525"/></svg>
        831.555.0147
      </li>
      <li class="upper">
        <svg class="icon" viewBox="0 0 20 20"><circle cx="10" cy="10" r="10" fill="var(--green)"/><path d="M10 4.5 C7.6 4.5 6 6.2 6 8.3 C6 11 10 15.5 10 15.5 C10 15.5 14 11 14 8.3 C14 6.2 12.4 4.5 10 4.5 Z" fill="#252525"/><circle cx="10" cy="8.3" r="1.5" fill="var(--green)"/></svg>
        418 Juniper Ln, Felton, CA 95092
      </li>
    </ul>
  </section>
</body>
</html>
```